Innovative Educational Technology Startup needs Business Cards!

"Campus Horizon" is an all-in-one, social profile based, online portal for Companies and Students to connect and carry out their brand ambassadorship tasks and requirements. The service allows for companies to more efficiently deploy brand ambassadorship opportunities to the millions of students actively seeking on-campus work experience.

Both educational and corporate tied into one (please keep that in mind for design purposes)
Updates

Project Deadline Extended
Reason: Need time to provide feedback to the several great designs that have been created! Thanks for the patience of one more day!

Target Market(s)

Those who get the card will more than likely be business men and working adults, but many educational instructors, professors, students, marketers, and propoective collegiate students will be the main target for these cards.

Industry/Entity Type

Business

Requirements
Must have
• Our Icon-Sized Logo (CH) must be a focus in regards to imagery.
• Color scheme must be Tiffany Blue/Black/White..(base of the card either white or black).
• www.campushorizonhub.com located somewhere on it, but not the main point of the card. (Logo is for that)
Should not have
• Childish or Tech-Only appeal.
• Basic font.
• Rather there be as little asymmetry in the card shape as possible. (curved edges is fine)

```html
<!DOCTYPE html>
<html lang="en">
<head>
<meta charset="utf-8">
<title>Campus Horizon — Business Card</title>
<link rel="stylesheet" href="https://fonts.googleapis.com/css2?family=Libre+Baskerville:wght@400;700&display=swap">
<style>
  :root {
    --brand-blue: #1fa9e1;
    --brand-black: #231f20;
    --card-white: #f7f7f7;
    --text-grey: #3a3a3a;
    --stage-light: #f2f2f2;
    --stage-dark: #d6d6d6;
  }
  * { box-sizing: border-box; margin: 0; padding: 0; }
  html, body {
    width: 1200px;
    height: 900px;
    overflow: hidden;
  }
  body {
    background: radial-gradient(ellipse at 50% 40%, var(--stage-light) 0%, var(--stage-dark) 100%);
    font-family: "Libre Baskerville", Georgia, serif;
    position: relative;
  }
  .card {
    position: absolute;
    left: 290px;
    width: 620px;
    height: 354px;
    background: var(--card-white);
    box-shadow: 0 6px 18px rgba(0, 0, 0, 0.18);
    overflow: hidden;
  }
  .card--back { top: 70px; }
  .card--front { top: 476px; }

  /* brand lockup */
  .wordmark {
    display: flex;
    align-items: center;
    gap: 12px;
    color: var(--brand-black);
    font-weight: 400;
    white-space: nowrap;
  }
  .wordmark__square {
    display: block;
    background: var(--brand-blue);
  }
  .card--back .wordmark {
    position: absolute;
    left: 0; right: 0; top: 118px;
    flex-direction: column;
    gap: 18px;
    font-size: 30px;
    letter-spacing: 0.5px;
  }
  .card--back .wordmark__square { width: 62px; height: 62px; }

  .card--front .wordmark {
    position: absolute;
    left: 172px; top: 82px;
    font-size: 27px;
  }
  .card--front .wordmark__square { width: 44px; height: 44px; }

  /* accent bars */
  .bar { position: absolute; height: 18px; }
  .bar--blue { background: var(--brand-blue); left: 0; top: 136px; width: 152px; }
  .bar--black { background: var(--brand-black); right: 0; top: 46px; width: 140px; }

  /* person */
  .person { position: absolute; left: 200px; top: 236px; }
  .person__name { color: var(--brand-blue); font-weight: 700; font-size: 15px; white-space: nowrap; }
  .person__role { color: var(--text-grey); font-size: 13px; margin-top: 3px; }

  /* contact */
  .contact {
    position: absolute;
    left: 362px; top: 172px;
    list-style: none;
    color: var(--text-grey);
    font-size: 12px;
    line-height: 1.5;
    white-space: nowrap;
  }
  .contact__item { display: flex; align-items: flex-start; gap: 12px; }
  .contact__item--address { margin-bottom: 12px; }
  .contact__icon { width: 14px; height: 14px; flex: none; margin-top: 2px; fill: var(--brand-blue); }
</style>
</head>
<body>

  <section class="card card--back" aria-label="Business card back">
    <div class="wordmark">
      <span class="wordmark__square"></span>
      <span class="wordmark__name">Campus Horizon</span>
    </div>
  </section>

  <section class="card card--front" aria-label="Business card front">
    <span class="bar bar--black"></span>
    <span class="bar bar--blue"></span>

    <div class="wordmark">
      <span class="wordmark__square"></span>
      <span class="wordmark__name">Campus Horizon</span>
    </div>

    <div class="person">
      <p class="person__name">Daniel Reyes</p>
      <p class="person__role">President</p>
    </div>

    <ul class="contact">
      <li class="contact__item contact__item--address">
        <svg class="contact__icon" viewBox="0 0 14 14"><path d="M7 0a4.6 4.6 0 0 0-4.6 4.6C2.4 8.2 7 14 7 14s4.6-5.8 4.6-9.4A4.6 4.6 0 0 0 7 0zm0 6.6a2 2 0 1 1 0-4 2 2 0 0 1 0 4z"/></svg>
        <span>000 Harbor Crest Ave Suite 000,<br>Linden Bay, CA 90000</span>
      </li>
      <li class="contact__item">
        <svg class="contact__icon" viewBox="0 0 14 14"><path d="M1 5c0-2 2.5-3 6-3s6 1 6 3v1.2h-3V4.8H4v1.4H1zM3.5 7h7l1.5 5H2z"/></svg>
        <span>000 000 0000</span>
      </li>
      <li class="contact__item">
        <svg class="contact__icon" viewBox="0 0 14 14"><path d="M3.5 0h7v14h-7zm1 1.5v6h5v-6zm.6 7.5v1.2h1.2V9zm2.3 0v1.2h1.2V9zM5.1 11v1.2h1.2V11zm2.3 0v1.2h1.2V11z"/></svg>
        <span>000 000 0000</span>
      </li>
      <li class="contact__item">
        <svg class="contact__icon" viewBox="0 0 14 14"><path d="M0 3h14v9H0zm1.3 1.2v.3L7 8.3l5.7-3.8v-.3zm0 1.8v4.8h11.4V6L7 9.8z"/></svg>
        <span>name@campushorizon.co</span>
      </li>
      <li class="contact__item">
        <svg class="contact__icon" viewBox="0 0 14 14"><path d="M7 0a7 7 0 1 0 0 14A7 7 0 0 0 7 0zm0 1.3c.8 0 1.7 1.4 2 3.7H5c.3-2.3 1.2-3.7 2-3.7zM1.4 6.3h2.4a12 12 0 0 0 0 1.4H1.4a5.7 5.7 0 0 1 0-1.4zm3.7 0h3.8a11 11 0 0 1 0 1.4H5.1a11 11 0 0 1 0-1.4zm5.1 0h2.4a5.7 5.7 0 0 1 0 1.4h-2.4a12 12 0 0 0 0-1.4zM5 9h4c-.3 2.3-1.2 3.7-2 3.7S5.3 11.3 5 9z"/></svg>
        <span>www.campushorizonhub.com</span>
      </li>
    </ul>
  </section>

</body>
</html>
```